National Training and assessment company needs a website

Create a 4 page website, simple but professional, the company provides training services to industry, resumes'/ CVs, personnel skill assessment, workplace skills profiling and develops manufactures and supplies training equipment for electrical/engineering training, Company title is Corvan T Pty Ltd and also trades under RSK & Associates. letterheads etc all are done using dark green
Updates
Project Deadline Extended
Reason: Due to work commitments will be interstate from the 26/02 til 05/03/14
Target Market(s)
The market is broad covering the general public, secondary colleges and corporate sector
Industry/Entity Type
Training
Look and feel
Each slider illustrates characteristics of the customer's brand and the style your logo design should communicate.

```html
<!DOCTYPE html>
<html lang="en">
<head>
<meta charset="utf-8">
<title>RSK &amp; Associates</title>
<link href="https://fonts.googleapis.com/css2?family=Raleway:wght@300;400;500&display=swap" rel="stylesheet">
<style>
:root{
  --green:#0f8a12;
  --green-dark:#0b6e0e;
  --ink:#2b2b2b;
  --muted:#8a8a8a;
  --band:#f1f1f1;
  --footer:#343434;
  --footer-text:#dedede;
}
*{margin:0;padding:0;box-sizing:border-box}
html,body{width:772px;height:1200px;overflow:hidden;background:#fff}
body{font-family:'Raleway',sans-serif;color:var(--ink);position:relative}
.abs{position:absolute}
.brand{left:52px;top:16px;color:var(--green);font-weight:400}
.brand .trade{font-size:11px}
.brand .name{font-size:24px;line-height:28px;margin-top:2px;width:170px}
.brand .acn{font-size:10px;color:var(--ink);margin-top:6px}
.search{left:507px;top:24px;width:214px;height:27px;border:1px solid #d6d6d6;border-radius:5px;background:#f7f7f7;font-size:10px;color:#b5b5b5;padding:7px 8px}
.search svg{position:absolute;right:6px;top:6px}
.nav{top:86px;display:flex;font-size:13px;color:var(--ink)}
.nav a{position:absolute;text-decoration:none;color:inherit;white-space:nowrap}
.nav .active{color:var(--green)}
.nav .marker{position:absolute;left:460px;top:-7px;width:36px;height:2px;background:var(--green)}
.hero{left:0;top:112px;width:772px;height:348px;background:linear-gradient(100deg,#1fb3a5 0%,#2aa99a 30%,#9aa6a8 55%,#c9cfd2 75%,#e1e4e5 100%)}
.arrow{width:31px;height:35px;background:#1b1b1b;top:270px}
.caption{left:0;top:328px;width:491px;height:91px;background:rgba(25,25,25,.82);color:#fff}
.caption h2{position:absolute;left:53px;top:17px;font-size:16px;font-weight:400;letter-spacing:.3px}
.caption p{position:absolute;left:53px;top:42px;width:420px;font-size:10px;line-height:12.5px;font-weight:300}
.about-title{left:0;width:772px;top:503px;text-align:center;font-size:26px;font-weight:300}
.about-text{left:86px;width:600px;top:546px;text-align:center;font-size:12.5px;line-height:21px;color:var(--muted);font-weight:300}
.services{left:261px;top:597px;list-style:none;font-size:12.5px;line-height:20.5px;color:#555}
.services li::before{content:"";display:inline-block;border-left:4px solid var(--green);border-top:3px solid transparent;border-bottom:3px solid transparent;margin-right:6px;vertical-align:1px}
.btn{left:298px;top:700px;width:139px;height:35px;background:var(--green);color:#fff;font-size:12.5px;text-align:center;line-height:35px}
.band{left:0;top:760px;width:772px;height:178px;background:var(--band)}
.card{top:780px;width:149px}
.card .photo{height:101px}
.card p{margin-top:8px;font-size:9.5px;line-height:14px;color:var(--green);text-align:center;text-transform:uppercase}
.councils-title{left:0;width:772px;top:973px;text-align:center;font-size:26px;font-weight:300}
.council{top:1047px;font-size:11px;font-weight:500;color:#777;display:flex;align-items:center;gap:5px;white-space:nowrap}
.council i{display:inline-block;width:10px;height:10px;background:#bcbcbc}
.small-arrow{top:1048px;width:14px;height:14px;background:#777}
.footer{left:0;top:1109px;width:772px;height:91px;background:var(--footer);color:var(--footer-text)}
.footer nav{position:absolute;left:50px;top:24px;font-size:10px;display:flex;gap:12px}
.footer .copy{position:absolute;left:50px;top:47px;font-size:10px}
.social{top:32px;width:29px;height:29px;border-radius:50%;background:#6b6b6b;border:2px solid #8a8a8a}
</style>
</head>
<body>
<header>
  <div class="abs brand">
    <div class="trade">Corvan T Pty Ltd T/</div>
    <div class="name">RSK &amp; Associates</div>
    <div class="acn">ACN.184 320 961</div>
  </div>
  <div class="abs search">Search
    <svg width="15" height="15" viewBox="0 0 15 15"><circle cx="6" cy="6" r="4.5" fill="none" stroke="#222" stroke-width="2"/><line x1="9.3" y1="9.3" x2="13.5" y2="13.5" stroke="#222" stroke-width="2.4"/></svg>
  </div>
  <nav class="abs nav" style="left:0">
    <span class="marker"></span>
    <a class="active" style="left:460px">Home</a>
    <a style="left:523px">AboutUs</a>
    <a style="left:600px">Services</a>
    <a style="left:677px">Contact</a>
  </nav>
</header>

<section>
  <div class="abs hero" role="img" aria-label="Two engineers in hard hats reviewing a laptop beside industrial machinery"></div>
  <div class="abs arrow" style="left:8px"><svg width="31" height="35"><polyline points="18,9 12,17.5 18,26" fill="none" stroke="#fff" stroke-width="1.5"/></svg></div>
  <div class="abs arrow" style="left:733px"><svg width="31" height="35"><polyline points="13,9 19,17.5 13,26" fill="none" stroke="#fff" stroke-width="1.5"/></svg></div>
  <div class="abs caption">
    <h2>LOREM IPSUM DOLOR SIT</h2>
    <p>Lorem ipsum dolor sit amet, consectetur adipisicing elit, sed do eiusmod tempor incididunt ut&nbsp; amet, consectetur adipisicing elit, sed do eiusmod tempor incididunt ut</p>
  </div>
</section>

<section>
  <h1 class="abs about-title">About Company</h1>
  <p class="abs about-text">Corvan T Pty Ltd is dedicated to providing quality customer focused service in all its ventures.&nbsp; Corvan T core business is workplace training assessment with broader services which include</p>
  <ul class="abs services">
    <li>Employer Workplace skills profiling</li>
    <li>Employee skills profiling (Competency Profiling)</li>
    <li>Workplace training and Assessment</li>
    <li>Resume and Curricula Vita compilation</li>
  </ul>
  <div class="abs btn">KNOW MORE</div>
</section>

<section>
  <div class="abs band"></div>
  <div class="abs card" style="left:50px"><div class="photo" role="img" aria-label="Businessman climbing concrete steps under a blue sky" style="background:linear-gradient(90deg,#6d9fd6,#a9b0b3 60%,#8f8f8f)"></div><p>Employer workplace skills<br>profiling</p></div>
  <div class="abs card" style="left:224px"><div class="photo" role="img" aria-label="Group of smiling office professionals" style="background:linear-gradient(90deg,#9a8577,#d9d3ce 50%,#a07c66)"></div><p>Employer skills<br>profiling</p></div>
  <div class="abs card" style="left:397px"><div class="photo" role="img" aria-label="Trainer explaining to a colleague at a desk" style="background:linear-gradient(90deg,#e8ecef,#5f86b3 45%,#f2f2f2)"></div><p>Workplace training and<br>assessment</p></div>
  <div class="abs card" style="left:573px"><div class="photo" role="img" aria-label="Woman holding a folder in an office" style="background:linear-gradient(90deg,#cfd8dd,#e8d9c8 50%,#d7dde0)"></div><p>Resume and curricula vita<br>compilation</p></div>
</section>

<section>
  <h2 class="abs councils-title">Industry Skills Councils</h2>
  <div class="abs small-arrow" style="left:51px"><svg width="14" height="14"><polyline points="8.5,4 5,7 8.5,10" fill="none" stroke="#fff" stroke-width="1.3"/></svg></div>
  <div class="abs council" style="left:84px"><i></i>Fieldgrain</div>
  <div class="abs council" style="left:194px"><i></i>Buildmark</div>
  <div class="abs council" style="left:286px"><i></i>Corestone</div>
  <div class="abs council" style="left:388px"><i></i>Civic Skills</div>
  <div class="abs council" style="left:505px"><i></i>Tradewell</div>
  <div class="abs council" style="left:602px"><i></i>Servewise</div>
  <div class="abs small-arrow" style="left:707px"><svg width="14" height="14"><polyline points="5.5,4 9,7 5.5,10" fill="none" stroke="#fff" stroke-width="1.3"/></svg></div>
</section>

<footer class="abs footer">
  <nav><span>Home</span><span>AboutUs</span><span>Services</span><span>Training</span><span>News</span><span>Contact</span></nav>
  <div class="copy">All Rights rteserved. copyrights @ 2014</div>
  <span class="abs social" style="left:597px"></span>
  <span class="abs social" style="left:629px"></span>
  <span class="abs social" style="left:660px"></span>
  <span class="abs social" style="left:693px"></span>
</footer>
</body>
</html>
```